Debt Relief Landing Page Design

I need a landing page designed (and the accompanying Thank You page) for my client.

I have drafted the wireframes for the layout of the pages (attached) and need a professional looking finish.

The main colours to use are green and blue as per their current branding, see website for specifications - http://www.clearpathledger.com.au/

```html
<!DOCTYPE html>
<html lang="en">
<head>
<meta charset="utf-8">
<title>ClearPath Ledger – Debt Relief</title>
<link href="https://fonts.googleapis.com/css2?family=Roboto+Slab:wght@400;700&family=Roboto+Condensed:wght@400&family=Roboto:wght@500;700&family=Open+Sans:wght@400;600&display=swap" rel="stylesheet">
<style>
:root{
  --navy:#1b2f5e;
  --green:#5f9432;
  --green-light:#6aa33a;
  --page:#f8f8f8;
  --ink:#333333;
  --hero-dark:#3f3f3f;
  --form-grey:#b9b9b9;
  --white:#ffffff;
}
*{margin:0;padding:0;box-sizing:border-box}
html,body{width:739px;height:1200px;overflow:hidden;background:var(--page)}
.page{position:relative;width:739px;height:1200px;overflow:hidden;font-family:"Open Sans",sans-serif;color:var(--ink)}
.abs{position:absolute}

/* header */
.site-header{left:0;top:0;width:739px;height:65px;background:var(--page);border-top:1px solid #9aa39a;border-bottom:2px solid var(--green)}
.brand{left:48px;top:18px;font-family:"Roboto",sans-serif;font-weight:700;font-size:25px;letter-spacing:-1px;color:var(--navy);display:flex;align-items:center;gap:8px}
.brand-dot{width:12px;height:12px;background:var(--green);border-radius:50%}
.call{left:572px;top:25px;display:flex;gap:6px;align-items:center}
.call-text{font-family:"Roboto Slab",serif;color:var(--green);line-height:1.1}
.call-label{font-size:10px}
.call-number{font-family:"Roboto",sans-serif;font-weight:500;font-size:15px}

/* hero */
.hero{left:0;top:66px;width:739px;height:268px;background:linear-gradient(90deg,#5a5450 0%,#3e3e3e 35%,#474747 100%);border-bottom:2px solid var(--green)}
.hero-photo{left:0;top:66px;width:160px;height:268px;background:linear-gradient(160deg,#6a5c52,#2e2a28)}
.hero-copy{left:158px;top:84px;width:318px;color:var(--white);font-family:"Roboto Condensed",sans-serif}
.hero-title{font-size:25px;font-weight:400;line-height:1.15;margin-bottom:12px}
.hero-copy p{font-size:11.2px;line-height:14.5px;margin-bottom:8px}
.pointer{left:435px;top:296px}

.consult-form{left:484px;top:67px;width:206px;height:267px;background:var(--form-grey);border:3px solid var(--navy);border-bottom:none}
.form-head{background:var(--green);height:59px;padding:3px 7px 0 7px;color:var(--white);font-family:"Roboto Slab",serif}
.form-title{font-size:18px;line-height:22px;border-bottom:1px dashed #c9dcb5;padding-bottom:2px}
.form-sub{font-size:8.5px;line-height:11px;margin-top:4px;color:#253a1a}
.field{position:absolute;left:4px;display:flex;align-items:center;font-family:"Roboto Slab",serif;font-size:8.5px;line-height:9px;color:#333}
.field span{width:52px}
.field i{display:block;width:140px;height:16px;background:#bdbdbd;border:1px solid #8a8a8a}
.form-btn{left:12px;top:221px;width:180px;height:28px;background:var(--green);color:var(--white);font-family:"Roboto Slab",serif;font-size:11.5px;display:flex;align-items:center;justify-content:center}

/* services */
.section-title{font-family:"Roboto Slab",serif;font-size:14.5px;color:var(--navy);text-align:center;width:739px;left:0}
.section-title em{font-style:normal;color:var(--green)}
.dash{height:0;border-top:1px dashed #888}
.service{width:210px;text-align:center}
.service .icon{margin:0 auto;width:58px;height:58px}
.service h3{font-family:"Roboto Slab",serif;font-weight:400;font-size:12px;color:var(--ink);margin-top:12px}
.service p{font-size:10.4px;line-height:14.5px;margin-top:14px}
.cta{background:var(--green);color:var(--white);font-family:"Roboto Slab",serif;display:flex;align-items:center;justify-content:center;border-radius:3px;font-size:19px}

/* testimonials */
.reviews{left:0;top:818px;width:739px;height:348px;background:var(--navy)}
.review-title{color:var(--white)}
.review-sub{font-family:"Roboto Slab",serif;font-size:10px;color:var(--green-light);text-align:center;width:739px;left:0}
.quote{width:504px;color:var(--white);font-family:Arial,sans-serif;font-size:9.6px;line-height:13.6px}
.quote b{display:block;margin-top:8px;font-size:9.8px}
.qmark{color:#8d97b0;font-family:Georgia,serif;font-size:16px;line-height:0}
.avatar{width:68px;height:68px;border-radius:50%;border:2px solid #3f6f2a;background:radial-gradient(circle at 50% 40%,#c79a78,#5b7a4b)}
.site-footer{left:0;top:1166px;width:739px;height:34px;background:var(--green);color:var(--white);font-size:9px;font-weight:600;display:flex;align-items:center;justify-content:center;gap:8px}
</style>
</head>
<body>
<div class="page">

<header class="site-header abs"></header>
<div class="brand abs"><span class="brand-dot"></span>ClearPath Ledger</div>
<div class="call abs">
  <svg width="22" height="22" viewBox="0 0 22 22"><circle cx="11" cy="11" r="9.5" fill="none" stroke="#1b2f5e" stroke-width="1.3"/><path d="M8 6c-1 1-1 2 0 4l3 4c1.5 1.6 2.6 2 3.6 1.2l.8-.8-2-2-1 .8-2.6-3.4.9-.9-1.6-2.3z" fill="#1b2f5e"/></svg>
  <div class="call-text"><div class="call-label">Call Us Today</div><div class="call-number">1300 555 214</div></div>
</div>

<section class="hero abs"></section>
<div class="hero-photo abs" role="img" aria-label="Photo of a smiling consultant seated at a desk"></div>
<div class="hero-copy abs">
  <h1 class="hero-title">Looking to Consolidate Your Debts?</h1>
  <p>If you have over $10,000 In Debt, We Can Help you be Debt free in 3-5 Years.</p>
  <p>Ledger Advisors in Australia's debt help relief specialists. Through years of industry experience and knowledge, our team of debt management experts can actively advise you on how to get out of the red, fast.</p>
  <p>At Ledger Advisors we are able to actively rectify your debt problems by creating simple and affordable payment plans for all debts.</p>
  <p>For a free, no obligation consultation simply fill out the form on the right and we'll be in contact with you shortly.</p>
</div>
<svg class="pointer abs" width="62" height="28" viewBox="0 0 62 28"><path d="M2 8 L40 9 L38 2 L60 14 L38 26 L40 19 L2 20 Q8 14 2 8z" fill="none" stroke="#fff" stroke-width="1.4"/></svg>

<form class="consult-form abs">
  <div class="form-head">
    <div class="form-title">Free Consultaion</div>
    <div class="form-sub">Fill In The Form Below To Recieve Your Free, No Obligation Consulation</div>
  </div>
  <div class="field" style="top:72px"><span>Name</span><i></i></div>
  <div class="field" style="top:96px"><span>Phone</span><i></i></div>
  <div class="field" style="top:120px"><span>Email</span><i></i></div>
  <div class="field" style="top:145px"><span>PostCode</span><i></i></div>
  <div class="field" style="top:170px"><span>Unsecured Debt.</span><i></i></div>
  <div class="field" style="top:202px"><span>Preferred Call Time</span><i></i></div>
  <div class="form-btn abs">GET MY FREE CONSTULATION</div>
</form>

<h2 class="section-title abs" style="top:353px">Here Are just Some Of Our Debt <em>Relief Services</em></h2>
<div class="dash abs" style="left:218px;top:375px;width:372px"></div>

<div class="service abs" style="left:38px;top:401px">
  <svg class="icon" viewBox="0 0 58 58"><circle cx="29" cy="29" r="27.5" fill="#fff" stroke="#1b2f5e" stroke-width="2"/><path d="M22 30l8-9 3 3-2 3 4-1 3 4-9 10-6-2-2-5z" fill="#2b2b2b"/><circle cx="34" cy="18" r="3" fill="none" stroke="#2b2b2b" stroke-width="1.5"/></svg>
  <h3>Debt Consolidation Loans</h3>
  <p>Stop Getting hassed by creditors.Let us consolidate your personal debts into an easy repayment plan.</p>
</div>
<div class="service abs" style="left:270px;top:401px">
  <svg class="icon" viewBox="0 0 58 58"><circle cx="29" cy="29" r="27.5" fill="#fff" stroke="#1b2f5e" stroke-width="2"/><path d="M14 29 L29 16 L44 29 L40 29 L40 42 L18 42 L18 29z" fill="#2b2b2b"/><text x="29" y="39" text-anchor="middle" font-size="13" font-weight="700" fill="#fff" font-family="Arial">$</text></svg>
  <h3>Mortage Refinance</h3>
  <p>Consolidate your debt into available home loan equity, signnifically reducing your general repayment</p>
</div>
<div class="service abs" style="left:489px;top:401px">
  <svg class="icon" viewBox="0 0 58 58"><circle cx="29" cy="29" r="27.5" fill="#fff" stroke="#1b2f5e" stroke-width="2"/><rect x="14" y="20" width="26" height="18" fill="none" stroke="#2b2b2b" stroke-width="2"/><path d="M18 26h14M18 30h12M18 34h10" stroke="#2b2b2b" stroke-width="2"/><path d="M34 36l10-12 3 3-10 12-4 1z" fill="#2b2b2b"/></svg>
  <h3>Debt Agreements</h3>
  <p>A viable alternative to bankruptcy and debt consolidtaions loans</p>
</div>

<div class="service abs" style="left:38px;top:569px">
  <svg class="icon" viewBox="0 0 58 58"><circle cx="29" cy="29" r="27.5" fill="#fff" stroke="#1b2f5e" stroke-width="2"/><path d="M17 30l10 13 14-27-4 0-10 19-6-8z" fill="#2b2b2b"/><path d="M22 26v-6h3v9M27 24v-8h3v10M32 20v-6h3v4" stroke="#2b2b2b" stroke-width="2" fill="none"/></svg>
  <h3>Credit Repair</h3>
  <p>Assist you in removing unfair, disputable and incorrect information from your credit file / information, which you believe should not be there</p>
</div>
<div class="service abs" style="left:270px;top:569px">
  <svg class="icon" viewBox="0 0 58 58"><circle cx="29" cy="29" r="27.5" fill="#fff" stroke="#1b2f5e" stroke-width="2"/><rect x="17" y="22" width="4" height="20" fill="#2b2b2b"/><rect x="23" y="26" width="4" height="16" fill="#2b2b2b"/><rect x="29" y="30" width="4" height="12" fill="#2b2b2b"/><text x="39" y="28" text-anchor="middle" font-size="13" font-weight="700" fill="#2b2b2b" font-family="Arial">$</text><path d="M39 31v9M36 37l3 4 3-4" stroke="#2b2b2b" stroke-width="1.6" fill="none"/></svg>
  <h3>Bankruptcy</h3>
  <p>We will work with you yo accuartely determine if bankruptcy is the sole option of your situation</p>
</div>
<div class="service abs" style="left:489px;top:569px">
  <svg class="icon" viewBox="0 0 58 58"><circle cx="29" cy="29" r="27.5" fill="#fff" stroke="#1b2f5e" stroke-width="2"/><rect x="36" y="16" width="6" height="14" fill="#2b2b2b"/><path d="M34 16h-14c-2 0-3 2-3 3l-2 10c0 2 1 3 3 3h7l-2 7c0 3 3 4 4 2l7-10z" fill="#2b2b2b"/></svg>
  <h3>Bad Credit Loans</h3>
  <p>We Work in your best interests to provide a consilidtaion loan that turns yourbad credit history into a positive financial situation</p>
</div>

<div class="cta abs" style="left:238px;top:751px;width:299px;height:53px">GET MY FREE CONSTULATION</div>

<section class="reviews abs"></section>
<h2 class="section-title review-title abs" style="top:836px">We Make Our Clients' Happy</h2>
<div class="review-sub abs" style="top:857px">See What Our Say About us</div>
<div class="dash abs" style="left:226px;top:873px;width:288px;border-color:#c8cede"></div>

<svg class="abs" style="left:19px;top:959px" width="18" height="30" viewBox="0 0 18 30"><path d="M15 2 L3 15 L15 28" fill="none" stroke="#fff" stroke-width="2"/></svg>
<svg class="abs" style="left:691px;top:959px" width="18" height="30" viewBox="0 0 18 30"><path d="M3 2 L15 15 L3 28" fill="none" stroke="#fff" stroke-width="2"/></svg>

<div class="avatar abs" style="left:55px;top:897px" role="img" aria-label="Client portrait"></div>
<div class="quote abs" style="left:150px;top:901px">
  <span class="qmark">&ldquo;</span>&nbsp; We were on the verge of losing our car and did not know what to do, but now we are inan affordable arrangement to catch up ourcar payments and are on our way to a debt free future. We are even thinking of buying a house, without your help this would not be possible. <span class="qmark">&rdquo;</span>
  <b>Renata, Box Hill VIC</b>
</div>

<div class="quote abs" style="left:77px;top:993px">
  <span class="qmark">&ldquo;</span>&nbsp; We were on the verge of losing our car and did not know what to do, but now we are inan affordable arrangement to catch up ourcar payments and are on our way to a debt free future. We are even thinking of buying a house, without your help this would not be possible. <span class="qmark">&rdquo;</span>
  <b>Renata, Box Hill VIC</b>
</div>
<div class="avatar abs" style="left:591px;top:989px" role="img" aria-label="Client portrait"></div>

<div class="cta abs" style="left:226px;top:1101px;width:300px;height:53px">GET MY FREE CONSTULATION</div>

<footer class="site-footer abs"><span>© 2015 ClearPathLedger. All Rights Reserved</span><span>Privacy Policy</span><span>Terms &amp; Conditions</span></footer>

</div>
</body>
</html>
```